Awesome Business Card Design needed!

Hey there.
I'm looking for a simple but awesome business card design.
Type of company: Online advertisement agency
(please don't use the typical business people or statistics images on the card)
The front has to display the business name
and possibly some sort of logo ( perhaps something with the two M's of the biz name )
And the back of the card should say:
Name
Phone
Email
Let your imagination flow.
here are some designs that I like and that you can use as inspiration.
Simple but Awesome
http://images.pixelvantor.net/designs/55128_877673_43091_thumbnail.jpg
http://images.pixelvantor.net/designs/37714_747642_40106_image.jpg
http://images.pixelvantor.net/designs/55128_877673_43091_image.jpg
http://images.pixelvantor.net/designs/51321_781878_43091_image.jpg
http://images.pixelvantor.net/designs/33378_399063_15912_image.jpg
http://images.pixelvantor.net/designs/2337_271604_9495_image.jpg
good luck

```html
<!DOCTYPE html>
<html lang="en">
<head>
<meta charset="utf-8">
<title>Torvan Media – Business Card</title>
<link rel="stylesheet" href="https://fonts.googleapis.com/css2?family=Arimo&family=Poiret+One&display=swap">
<style>
  :root {
    --page-bg: #ffffff;
    --card-dark: #1f1b1a;
    --card-dark-glow: #2a2624;
    --card-light: #ffffff;
    --card-edge: #6f6f6f;
    --ink-light: #ffffff;
    --ink-muted: #8c8c8c;
    --band-dark: #1c1817;
    --band-glow: #3a3533;
  }
  html, body {
    margin: 0;
    padding: 0;
    width: 953px;
    height: 1200px;
    overflow: hidden;
    background: var(--page-bg);
  }
  .sheet {
    position: relative;
    width: 953px;
    height: 1200px;
  }
  .card {
    position: absolute;
    left: 51px;
    width: 865px;
    height: 507px;
    border-radius: 30px;
    overflow: hidden;
    box-shadow: 0 12px 40px rgba(0, 0, 0, 0.16), 0 2px 8px rgba(0, 0, 0, 0.08);
  }
  .card--front {
    top: 38px;
    background: var(--card-dark);
  }
  .card--back {
    top: 642px;
    background: var(--card-light);
    border: 1px solid var(--card-edge);
    box-sizing: border-box;
    overflow: visible;
  }
  .front-glow {
    position: absolute;
    inset: 0;
  }
  .brand-name {
    position: absolute;
    right: 55px;
    top: 424px;
    margin: 0;
    font-family: "Poiret One", sans-serif;
    font-weight: 400;
    font-size: 40px;
    line-height: 1;
    color: var(--ink-light);
    letter-spacing: 0.5px;
  }
  .name-band {
    position: absolute;
    left: 338px;
    top: 245px;
    width: 530px;
    height: 62px;
    background:
      radial-gradient(ellipse 260px 90px at 330px -20px, var(--band-glow) 0%, rgba(58, 53, 51, 0.55) 55%, rgba(58, 53, 51, 0) 100%),
      linear-gradient(90deg, var(--band-dark) 0%, #26211f 60%, var(--band-dark) 100%);
    box-shadow: 0 6px 10px rgba(0, 0, 0, 0.25);
  }
  .holder-name {
    position: absolute;
    left: 20px;
    top: 6px;
    margin: 0;
    font-family: "Arimo", sans-serif;
    font-weight: 400;
    font-size: 44px;
    line-height: 1;
    color: var(--ink-light);
  }
  .contact {
    position: absolute;
    left: 346px;
    top: 330px;
    margin: 0;
    padding: 0;
    list-style: none;
    font-family: "Arimo", sans-serif;
    font-size: 24px;
    line-height: 45px;
    color: var(--ink-muted);
    text-shadow: 0 2px 3px rgba(0, 0, 0, 0.25);
  }
</style>
</head>
<body>
  <main class="sheet">
    <section class="card card--front" aria-label="Card front">
      <svg class="front-glow" width="865" height="507" viewBox="0 0 865 507" aria-hidden="true">
        <defs>
          <radialGradient id="glowFill" cx="0.45" cy="0.4" r="0.7">
            <stop offset="0" stop-color="#231f1e"/>
            <stop offset="1" stop-color="#2b2725"/>
          </radialGradient>
        </defs>
        <ellipse cx="187" cy="125" rx="428" ry="395" fill="url(#glowFill)"/>
      </svg>
      <p class="brand-name">Torvan Media</p>
    </section>

    <section class="card card--back" aria-label="Card back">
      <div class="name-band">
        <p class="holder-name">name</p>
      </div>
      <ul class="contact">
        <li>telp</li>
        <li>email</li>
      </ul>
    </section>
  </main>
</body>
</html>
```